Ross Whitcombe Voice Talent Postcard Design

Need a postcard design for an individual Voice Actor to send out to clients. Would like to see designs utilize the provided logo and its colors. The final design should communicate a voice that is conversational, friendly, fresh and professional. These postcards are intended to be sent out to existing clients simply as reminders that I exist after we've worked on projects together.

Requirements
Must have
• Must incorporate the sine wave with the "A" in the middle. The website address is: www.rosswhitcombe-vo.example.
Nice to have
• Please no microphone images. Please experiment graphically with the logo provided. This is a graphic heavy postcard. The only text is "Ross Whitcombe Voice Talent," and "www.rosswhitcombe-vo.example"
Should not have
• no pictures of me or microphones.

```html
<!DOCTYPE html>
<html lang="en">
<head>
<meta charset="UTF-8">
<title>Ross Whitcombe Voice Talent Postcard</title>
<link rel="stylesheet" href="https://fonts.googleapis.com/css2?family=Raleway:wght@300;400;600&display=swap">
<style>
  :root {
    --stage: #1c1c1c;
    --card: #ffffff;
    --sky: #1aa3dc;
    --ink: #1e1e1e;
    --rule: #b9b9b9;
    --stamp-edge: #cfcfcf;
  }
  * { box-sizing: border-box; margin: 0; padding: 0; }
  html, body { width: 900px; height: 1200px; overflow: hidden; }
  body {
    background: var(--stage);
    font-family: "Raleway", Arial, sans-serif;
    position: relative;
  }
  .postcard {
    position: absolute;
    left: 99px;
    width: 705px;
    background: var(--card);
    overflow: hidden;
    box-shadow: 0 6px 18px rgba(0,0,0,0.5);
  }
  .postcard--front { top: 45px; height: 540px; }
  .postcard--back { top: 621px; height: 495px; }

  .sky-band { position: absolute; left: 0; top: 0; width: 100%; background: var(--sky); }
  .divider { position: absolute; left: 0; width: 100%; background: var(--card); }
  .ink-band { position: absolute; left: 0; width: 100%; background: var(--ink); }

  .postcard--front .sky-band { height: 186px; }
  .postcard--front .divider { top: 186px; height: 9px; }
  .postcard--front .ink-band { top: 195px; height: 66px; }
  .postcard--back .sky-band { height: 111px; }
  .postcard--back .divider { top: 111px; height: 9px; }
  .postcard--back .ink-band { top: 120px; height: 63px; }

  .brand-mark {
    position: absolute;
    display: flex; align-items: center; gap: 14px;
    color: var(--card);
    font-weight: 600;
    text-transform: uppercase;
    white-space: nowrap;
  }
  .brand-mark__square { display: block; background: var(--card); }
  .postcard--front .brand-mark {
    left: 0; right: 0; top: 128px; justify-content: center;
    font-size: 30px; letter-spacing: 5px;
  }
  .postcard--front .brand-mark__square { width: 26px; height: 26px; }
  .postcard--back .brand-mark {
    left: 36px; top: 70px;
    font-size: 20px; letter-spacing: 3px; gap: 10px;
  }
  .postcard--back .brand-mark__square { width: 18px; height: 18px; }

  .identity {
    position: absolute; left: 0; right: 0; top: 298px;
    text-align: center; color: var(--ink);
  }
  .identity__name {
    font-size: 60px; font-weight: 400; letter-spacing: 1px; line-height: 1;
    text-transform: uppercase;
  }
  .identity__role {
    margin-top: 12px;
    font-size: 50px; font-weight: 300; letter-spacing: 13px; line-height: 1;
    text-transform: uppercase;
  }
  .website {
    position: absolute; left: 0; right: 0; top: 482px;
    text-align: center; color: var(--sky);
    font-size: 24px; font-weight: 400; letter-spacing: 1px;
  }

  .stamp-box {
    position: absolute; right: 9px; top: 3px;
    width: 174px; height: 171px;
    background: var(--card);
    border: 3px solid var(--stamp-edge);
    border-radius: 6px;
  }
  .address-lines {
    position: absolute; left: 345px; top: 327px; width: 336px;
    display: flex; flex-direction: column; gap: 46px;
  }
  .address-lines span { display: block; height: 2px; background: var(--rule); }
</style>
</head>
<body>
  <section class="postcard postcard--front">
    <div class="sky-band"></div>
    <div class="divider"></div>
    <div class="ink-band"></div>
    <div class="brand-mark"><span class="brand-mark__square"></span>Ross Whitcombe</div>
    <div class="identity">
      <h1 class="identity__name">Ross Whitcombe</h1>
      <p class="identity__role">Voice Talent</p>
    </div>
    <p class="website">www.rosswhitcombe-vo.example</p>
  </section>

  <section class="postcard postcard--back">
    <div class="sky-band"></div>
    <div class="divider"></div>
    <div class="ink-band"></div>
    <div class="brand-mark"><span class="brand-mark__square"></span>Ross Whitcombe</div>
    <div class="stamp-box"></div>
    <div class="address-lines">
      <span></span><span></span><span></span>
    </div>
  </section>
</body>
</html>
```